Copper Gate Labradoodle web design

We're a new labradoodle breeder in Charleston, SC in need of a web design.

Our name is Copper Gate Labradoodles.

Site we like: http://www.fernhilldoodlery.example/
http://www.quailbrookpups.example/

Logo Font:
The ''Copper Gate'' font is called TestarossaNF and is available freely at http://www.typequarry.example/testarossa-nf.font.  The ''Labradoodles'' font is called Worstveld Sling Extra and is available freely at http://www.glyphbarn.example/WorstveldSlingExtra.php.

Requirements
Must have
• Our logo
1. Home page
2. Labradoodle F.A.Q.
3. Our doodles
4. Availability
5. Adoption Process
6. Contact us
Link/badge icon for Health Guarantee
Nice to have
• Color and font to match the logo.

An area to add pictures
Should not have
• Rainbows
Rainbow colors

```html
<!DOCTYPE html>
<html lang="en">
<head>
<meta charset="utf-8">
<title>Copper Gate Labradoodles</title>
<link rel="stylesheet" href="https://fonts.googleapis.com/css2?family=Source+Sans+3:wght@300;400;600&family=Vollkorn:wght@600&display=swap">
<style>
:root{
  --cream:#f3f0e9;
  --pink:#f07a93;
  --pink-light:#f38da3;
  --pink-deep:#c8304e;
  --brown:#4a2a10;
  --brown-dark:#3a200a;
  --text:#4b3524;
  --muted:#7a6454;
  --white:#ffffff;
}
*{box-sizing:border-box;margin:0;padding:0}
html,body{width:1051px;height:1200px;overflow:hidden}
body{position:relative;font-family:"Source Sans 3",sans-serif;color:var(--text);
  background:linear-gradient(to bottom,var(--cream) 0,var(--cream) 330px,#e9e4d8 403px,var(--pink) 403px,var(--pink) 100%)}
.top-edge{position:absolute;left:0;top:0;width:100%;height:7px;background:var(--brown)}
.follow{position:absolute;left:881px;top:86px;font-size:11.5px;color:var(--muted)}
.social-dot{position:absolute;left:937px;top:76px;width:28px;height:28px;border-radius:50%;background:var(--brown)}
.panel{position:absolute;left:75px;top:114px;width:900px;height:900px;background:var(--white);border-radius:4px 4px 0 0}
.panel-curve{position:absolute;left:75px;top:1012px}
.nav{position:absolute;left:75px;top:114px;width:900px;height:49px;background:linear-gradient(var(--pink-light),var(--pink));border-radius:4px 4px 0 0}
.nav .group{position:absolute;top:15px;display:flex}
.nav a{color:var(--white);text-decoration:none;font-size:15.5px;padding:0 11px;border-left:1px solid rgba(255,255,255,.45);line-height:19px}
.nav a.first{border-left:0}
.nav .left{left:13px}
.nav .right{left:554px}
.logo{position:absolute;left:432px;top:18px;width:186px;height:180px;border-radius:50%;background:var(--cream);display:flex;align-items:center;justify-content:center;text-align:center;z-index:3}
.logo span{font-family:"Vollkorn",serif;font-weight:600;font-size:20px;line-height:1.2;color:var(--brown)}
.slider{position:absolute;left:87px;top:172px;width:876px;height:354px;background:var(--brown)}
.slide-photo{position:absolute;left:12px;top:9px;width:852px;height:335px;border:2px solid #e8e2da;background:radial-gradient(ellipse at 60% 45%,#f4f1ec 0,#e0dbd2 30%,#8a7a6a 70%,#4a3428 100%)}
.arrow{position:absolute;top:140px}
.dots-tab{position:absolute;left:396px;top:320px;width:84px;height:34px;background:var(--brown);border-radius:20px 20px 0 0;display:flex;gap:6px;justify-content:center;padding-top:10px}
.dots-tab i{width:9px;height:9px;border-radius:50%;background:#7a5e48}
.dots-tab i.on{background:var(--white)}
h2{font-family:"Vollkorn",serif;font-weight:600;font-size:21px;color:var(--brown);position:absolute;line-height:1}
.welcome-h{left:103px;top:552px}
.welcome-photo{position:absolute;left:103px;top:584px;width:173px;height:148px;border-radius:4px;background:linear-gradient(160deg,#8a9a6a,#e8e2da 50%,#6c7a4a)}
.welcome-text{position:absolute;left:289px;top:585px;width:362px}
.welcome-text .lead{font-size:13.8px;font-weight:400;color:var(--text);line-height:18px;margin-bottom:5px}
.welcome-text p{font-size:11.3px;font-weight:300;line-height:17.5px;color:var(--muted);margin-bottom:9px}
.rule{position:absolute;left:103px;top:766px;width:564px;height:1px;background:#ddd}
.vrule{position:absolute;left:673px;top:552px;width:1px;height:424px;background:#ddd}
.card{position:absolute;top:784px;width:272px;height:174px;border-radius:3px;overflow:hidden}
.card .bar{position:absolute;left:0;bottom:0;width:100%;height:39px;background:rgba(245,242,236,.9);display:flex;align-items:center;padding-left:10px;font-size:17px;color:var(--text)}
.play-sm{width:24px;height:24px;border-radius:50%;background:var(--white);margin-right:10px;display:flex;align-items:center;justify-content:center}
.blog{left:101px;background:linear-gradient(#5a7a30,#8aa050 50%,#e8e0c8)}
.apply{left:383px;background:linear-gradient(135deg,#e88aa0,#e8d0c0 45%,#c89878)}
.video-h{left:696px;top:552px}
.video{position:absolute;left:696px;top:581px;width:262px;height:171px;border:2px solid #e8e4e0;border-radius:3px;background:linear-gradient(120deg,#9a80d8 0,#c8c0b8 45%,#e8d8b8 75%,#8a7a6a)}
.play-lg{position:absolute;left:111px;top:66px}
.contact{position:absolute;left:695px;top:788px;width:262px;height:171px;background:linear-gradient(var(--brown),var(--brown-dark));border-radius:2px;padding:22px 20px}
.contact h3{font-family:"Vollkorn",serif;font-weight:600;font-size:21px;color:var(--white);line-height:1}
.contact p{font-size:11px;font-weight:300;color:#e8dcd0;line-height:15px;margin-top:4px;width:200px}
.email{margin-top:8px;height:30px;border:1px solid #7a5a3a;border-radius:3px;background:rgba(255,255,255,.08);font-size:12px;font-style:italic;font-weight:300;color:#e8dcd0;padding:6px 12px}
.subscribe{position:absolute;left:151px;top:119px;width:97px;height:31px;border-radius:4px;background:linear-gradient(var(--pink-light),var(--pink));border:1px solid #f7b8c6;color:var(--brown);font-size:15px;text-align:center;line-height:29px}
.badge{position:absolute;left:452px;top:992px;width:148px;height:92px;border-radius:10px;background:var(--pink-deep);border:2px solid #f5a8b8;display:flex;flex-direction:column;align-items:center;justify-content:center;color:var(--white);font-weight:600;text-decoration:none;line-height:1.05}
.badge .small{font-size:15px}
.badge .big{font-size:21px}
.footer-nav{position:absolute;left:0;top:1103px;width:1051px;display:flex;justify-content:center}
.footer-nav a{color:var(--white);text-decoration:none;font-size:13px;padding:0 9px;border-left:1px solid var(--white);line-height:14px}
.footer-nav a.first{border-left:0}
.copyright{position:absolute;left:0;top:1130px;width:1051px;text-align:center;font-size:10.5px;font-weight:300;color:#fbd8e0}
</style>
</head>
<body>
<div class="top-edge"></div>
<div class="follow">Follow Us</div>
<div class="social-dot"></div>

<div class="panel"></div>
<svg class="panel-curve" width="900" height="24" viewBox="0 0 900 24"><path d="M0 0 H900 V0 Q450 36 0 0 Z" fill="#fff"/></svg>

<nav class="nav">
  <div class="group left"><a class="first">Home page</a><a>Labradoodle F.A.Q.</a><a>Our doodles</a></div>
  <div class="group right"><a class="first">Availability</a><a>Adoption Process</a><a>Contact us</a></div>
</nav>
<div class="logo"><span>Copper Gate<br>Labradoodles</span></div>

<section class="slider">
  <div class="slide-photo" role="img" aria-label="Photo of a white labradoodle sitting on carpet"></div>
  <svg class="arrow" style="left:36px" width="28" height="56" viewBox="0 0 28 56"><path d="M26 2 L3 28 L26 54" fill="none" stroke="#fff" stroke-width="2"/></svg>
  <svg class="arrow" style="left:830px" width="28" height="56" viewBox="0 0 28 56"><path d="M2 2 L25 28 L2 54" fill="none" stroke="#fff" stroke-width="2"/></svg>
  <div class="dots-tab"><i class="on"></i><i></i><i></i><i></i></div>
</section>

<h2 class="welcome-h">Welcome to Our Website Mainpage</h2>
<div class="welcome-photo" role="img" aria-label="Photo of a small white puppy on grass"></div>
<div class="welcome-text">
  <div class="lead">Mauris vel lacus vitae felis vestibulum volutpat.</div>
  <p>Etiam est nunc, venenatis in, tristique eu, imperdiet ac, nisl. Cum sociis natoque penatibus et magnis dis parturient montes, nascetur ridiculus mus. In iaculis facilisis massa. Etiam eu urna. Sed porta. Suspendisse quam leo, molestie sed, luctus quis, feugiat in, pede. Fusce tellus.</p>
  <p>Sed metus augue, convallis et, vehicula ut, pulvinar eu, ante. Integer orci tellus, tristique vitae, consequat nec, porta vel, lectus.</p>
</div>
<div class="rule"></div>
<div class="vrule"></div>

<a class="card blog" role="img" aria-label="Photo of a cream puppy lying in grass">
  <div class="bar"><span class="play-sm"><svg width="8" height="10"><path d="M0 0 L8 5 L0 10Z" fill="#3a200a"/></svg></span>Blog</div>
</a>
<a class="card apply" role="img" aria-label="Photo of a child resting with a puppy">
  <div class="bar"><span class="play-sm"><svg width="8" height="10"><path d="M0 0 L8 5 L0 10Z" fill="#3a200a"/></svg></span>Puppy Application</div>
</a>

<h2 class="video-h">Watch Video</h2>
<div class="video" role="img" aria-label="Video still of a person giving a treat to a labrador">
  <svg class="play-lg" width="40" height="40" viewBox="0 0 40 40"><circle cx="20" cy="20" r="19" fill="#222" stroke="#fff" stroke-width="2"/><path d="M15 12 L28 20 L15 28Z" fill="#fff"/></svg>
</div>

<div class="contact">
  <h3>Contact Us</h3>
  <p>Please sign up here your email address for contact us</p>
  <div class="email">email address</div>
  <div class="subscribe">Subscribe</div>
</div>

<a class="badge"><span class="small">HEALTH</span><span class="big">GUARANTEE</span></a>

<footer>
  <nav class="footer-nav">
    <a class="first">Home page</a><a>Labradoodle F.A.Q.</a><a>Our doodles</a><a>Availability</a><a>Adoption Process</a><a>Puppy Application</a><a>Health Guarantee</a><a>Contact us</a>
  </nav>
  <div class="copyright">© 2013 Company Name.&nbsp; All right reserved. Term of Use</div>
</footer>
</body>
</html>
```